Make existing 'Send In Blue' marketing email look fantastic

I have an existing marketing email template that advertises a webinar, designed in Send In Blue, that needs a makeover. Some elements that can't be changed is the text, the company logo, and the main photo, but anything else can be changed in the email to make a better design.

Contest winner must help to import the finished template into my 'Send In Blue' account so that it is ready to go.

See the existing marketing email template in the file below.

```html
<!DOCTYPE html>
<html lang="en">
<head>
<meta charset="utf-8">
<title>Webinar Announcement – Quiet Voices Clinic</title>
<link href="https://fonts.googleapis.com/css2?family=Montserrat:wght@400;500;600;700&family=Roboto:wght@700&display=swap" rel="stylesheet">
<style>
:root{
  --page:#f1d9da;
  --shadow:#e5cfd0;
  --white:#ffffff;
  --ink:#1f1f1f;
  --grey:#6f6f6f;
  --light-grey:#9a9a9a;
  --green:#8aa84a;
  --blue:#5b95d6;
  --link:#2f6fc4;
  --mauve:#d3bbbf;
  --mauve-light:#f3dedd;
  --header:#282828;
}
*{margin:0;padding:0;box-sizing:border-box}
html,body{width:1200px;height:3873px;overflow:hidden}
body{background:var(--page);font-family:"Montserrat",sans-serif;color:var(--ink);position:relative}
.backing{position:absolute;left:224px;top:105px;width:793px;height:3438px;background:var(--shadow)}
.email{position:absolute;left:194px;top:78px;width:794px;height:3420px;background:var(--white);overflow:hidden}
.email > *{position:absolute}
.center{left:0;width:100%;text-align:center}

.header{left:0;top:0;width:100%;height:113px;background:var(--header);display:flex;align-items:center;justify-content:center;gap:12px}
.header .mark{width:40px;height:40px;border-radius:50%;background:var(--green)}
.header .brand{color:var(--white);font-size:22px;font-weight:500;letter-spacing:1px}

.title{top:144px;font-family:"Roboto",sans-serif;font-size:48px;line-height:56px;color:var(--green)}
.intro{top:212px;left:40px;width:714px;text-align:center;font-size:22px;line-height:35px;letter-spacing:1.6px;color:var(--grey)}
.hero{left:0;top:345px;width:100%;height:609px;background:linear-gradient(160deg,#f3ecd8 0%,#d9cfb6 35%,#7fa4d8 70%,#5b86c8 100%)}

.topic{top:1000px;font-size:32px;line-height:40px;font-weight:600;letter-spacing:.5px}
.topic span{color:var(--blue);font-weight:500}

.fact{top:1112px;width:220px;text-align:center}
.fact svg{display:block;margin:0 auto}
.fact p{margin-top:14px;font-size:20px;line-height:26px;letter-spacing:1px;font-weight:500}
.fact.date{left:54px}.fact.time{left:289px}.fact.place{left:523px}

.visual{left:50px;top:1348px;width:258px;height:258px;background:var(--mauve)}
.visual-frame{left:78px;top:1376px;width:259px;height:261px;border-right:3px solid #555;border-bottom:3px solid #555}
.visual-frame::before{content:"";position:absolute;left:0;top:0;width:3px;height:100%;background:#555;clip-path:inset(230px 0 0 0)}
.visual-frame::after{content:"";position:absolute;right:-3px;top:0;width:30px;height:3px;background:#555}
.about{left:362px;top:1398px;width:388px;font-size:13.5px;line-height:17.5px;color:var(--grey);text-align:justify}
.about p+p{margin-top:17px}

.includes-title{left:50px;top:1708px;font-size:25px;line-height:32px;font-weight:500}
.item{left:50px;width:700px;padding-left:28px;font-size:13.5px;line-height:17px;color:var(--grey)}
.item svg{position:absolute;left:0;top:14px}
.join{left:50px;top:2027px;width:700px;font-size:13.5px;line-height:17px;color:var(--grey)}

.price-frame{left:113px;top:2148px;width:612px;height:292px;border:3px solid var(--mauve)}
.price-box{left:95px;top:2128px;width:613px;height:294px;background:var(--mauve)}
.price{top:2170px;width:300px;text-align:center}
.price.standard{left:86px}.price.early{left:408px}
.price .art{width:96px;height:96px;margin:0 auto;border-radius:50%}
.price.standard .art{background:linear-gradient(135deg,#f2c7a0,#4a6a9a)}
.price.early .art{background:linear-gradient(135deg,#9cc0ef,#4f86cf)}
.price h3{margin-top:26px;font-size:21px;line-height:26px;font-weight:500;letter-spacing:1px}
.price p{margin-top:6px;font-size:14px;line-height:22px;letter-spacing:1px;color:#8a7d80}
.deadline{left:182px;top:2423px;width:439px;height:27px;background:var(--green);color:var(--white);font-size:15.5px;line-height:27px;letter-spacing:1.5px;text-align:center}

.more{top:2490px;font-size:18px;line-height:27px;letter-spacing:1px}
.more a{color:var(--link);text-decoration:none;font-weight:500}
.rule{left:39px;width:701px;height:2px;background:var(--mauve-light)}
.alt-title{top:2633px;font-size:22px;line-height:28px;font-weight:700;color:var(--green)}
.alt-body{left:55px;top:2676px;width:684px;text-align:center;font-size:13.5px;line-height:17.5px;color:var(--grey)}
.series{left:55px;top:2825px;width:684px;text-align:center;font-size:13.5px;line-height:18px;color:var(--grey)}
.series p+p{margin-top:16px}
.series a{color:var(--link)}

.footer{left:0;top:2981px;width:100%;height:271px;background:var(--mauve);text-align:center;font-size:16px;line-height:22px;letter-spacing:.8px}
.footer p{position:absolute;left:0;width:100%}
.footer a{color:var(--link);text-decoration:none}
.footer .unsub a{text-decoration:underline}

.follow{top:3292px;font-size:20px;line-height:28px;letter-spacing:4px;font-weight:500}
.social{top:3340px;left:315px;display:flex;gap:40px}
.social span{width:28px;height:28px;border-radius:50%;background:#111}
</style>
</head>
<body>
<div class="backing"></div>
<main class="email">
  <header class="header"><span class="mark"></span><span class="brand">QUIET VOICES CLINIC</span></header>

  <h1 class="title center">Webinar Announcement</h1>
  <p class="intro">The next webinar by the Quiet Voices Clinic is about an intensive School program for Children with Selective Mutism</p>

  <div class="hero" role="img" aria-label="Photo of a young girl sitting at her desk in a bright classroom while classmates raise their hands"></div>

  <h2 class="topic center">TREATMENT FOR SELECTIVE MUTISM<br>IN <span>SCHOOLS AND PRESCHOOLS</span></h2>

  <div class="fact date">
    <svg width="116" height="116" viewBox="0 0 116 116"><circle cx="52" cy="52" r="50" fill="#f6e4e0"/><circle cx="60" cy="60" r="52" fill="#d3bbbf"/>
      <rect x="36" y="38" width="48" height="44" rx="6" fill="none" stroke="#222" stroke-width="4"/><rect x="36" y="38" width="48" height="11" fill="#222"/>
      <rect x="44" y="32" width="4" height="12" fill="#222"/><rect x="72" y="32" width="4" height="12" fill="#222"/>
      <g fill="#222"><rect x="43" y="55" width="7" height="6"/><rect x="53" y="55" width="7" height="6"/><rect x="63" y="55" width="7" height="6"/><rect x="73" y="55" width="5" height="6"/><rect x="43" y="66" width="7" height="6"/><rect x="53" y="66" width="7" height="6"/><rect x="63" y="66" width="7" height="6"/><rect x="73" y="66" width="5" height="6"/></g></svg>
    <p>THURS 23RD<br>MARCH 2023</p>
  </div>
  <div class="fact time">
    <svg width="116" height="116" viewBox="0 0 116 116"><circle cx="52" cy="52" r="50" fill="#f6e4e0"/><circle cx="60" cy="60" r="52" fill="#8aa84a"/>
      <circle cx="60" cy="60" r="28" fill="none" stroke="#222" stroke-width="5"/><path d="M60 42v18l12 8" fill="none" stroke="#222" stroke-width="4" stroke-linecap="round"/></svg>
    <p>5PM TO 8PM</p>
  </div>
  <div class="fact place">
    <svg width="116" height="116" viewBox="0 0 116 116"><circle cx="52" cy="52" r="50" fill="#f6e4e0"/><circle cx="60" cy="60" r="52" fill="#5b95d6"/>
      <path d="M60 30c-11 0-19 8-19 19 0 14 19 32 19 32s19-18 19-32c0-11-8-19-19-19z" fill="#222"/><circle cx="60" cy="49" r="7" fill="#5b95d6"/><ellipse cx="60" cy="86" rx="16" ry="4" fill="none" stroke="#222" stroke-width="3"/></svg>
    <p>WEBINAR</p>
  </div>

  <div class="visual-frame"></div>
  <div class="visual" role="img" aria-label="Supporting image area for the webinar"></div>
  <div class="about">
    <p>Selective Mutism is a treatable anxiety disorder but generally takes 1-2 years of treatment to resolve, and requires an intensive school or preschool program.</p>
    <p>This 3-hour webinar is for teachers and support staff who have a preschool or primary-aged child with Selective Mutism.</p>
    <p>Learn about why some children are unable to talk in school to adults and/or peers or are very reluctant to talk, and specific strategies to gradually enable them to become confident communicators at school with all teachers and peers and evenutally give class speeches!</p>
  </div>

  <h2 class="includes-title">The webinar includes the following components:</h2>
  <p class="item" style="top:1766px"><svg width="13" height="13" viewBox="0 0 13 13"><rect x=".5" y=".5" width="12" height="12" fill="none" stroke="#5b95d6"/><path d="M3 6.5l2.5 2.5L11 2" fill="none" stroke="#5b95d6" stroke-width="1.6"/></svg>A ‘5-stage Model of Communication’ that underlies the treatment program</p>
  <p class="item" style="top:1801px"><svg width="13" height="13" viewBox="0 0 13 13"><rect x=".5" y=".5" width="12" height="12" fill="none" stroke="#5b95d6"/><path d="M3 6.5l2.5 2.5L11 2" fill="none" stroke="#5b95d6" stroke-width="1.6"/></svg>Factors that make it harder or easier for children to talk</p>
  <p class="item" style="top:1836px"><svg width="13" height="13" viewBox="0 0 13 13"><rect x=".5" y=".5" width="12" height="12" fill="none" stroke="#5b95d6"/><path d="M3 6.5l2.5 2.5L11 2" fill="none" stroke="#5b95d6" stroke-width="1.6"/></svg>A ‘fading’ strategy involving the classroom teacher and parent that helps the child start to use their voice with their teacher</p>
  <p class="item" style="top:1888px"><svg width="13" height="13" viewBox="0 0 13 13"><rect x=".5" y=".5" width="12" height="12" fill="none" stroke="#5b95d6"/><path d="M3 6.5l2.5 2.5L11 2" fill="none" stroke="#5b95d6" stroke-width="1.6"/></svg>Strategies to generalise the child's talking to each peer in the classroom, then in small groups and whole class activities</p>
  <p class="item" style="top:1940px"><svg width="13" height="13" viewBox="0 0 13 13"><rect x=".5" y=".5" width="12" height="12" fill="none" stroke="#5b95d6"/><path d="M3 6.5l2.5 2.5L11 2" fill="none" stroke="#5b95d6" stroke-width="1.6"/></svg>Strategies to help the child generalise their talking to other teachers and staff and in their specialist classes</p>
  <p class="item" style="top:1992px"><svg width="13" height="13" viewBox="0 0 13 13"><rect x=".5" y=".5" width="12" height="12" fill="none" stroke="#5b95d6"/><path d="M3 6.5l2.5 2.5L11 2" fill="none" stroke="#5b95d6" stroke-width="1.6"/></svg>How to help a child with Selective Mutism transition to a new teacher and new school year</p>
  <p class="join">Join Margaret Ellison, Clinical Psychologist and Director of the Quiet Voices Clinic, to find out more about what you can do to help kids with Selective Mutism at school.</p>

  <div class="price-frame"></div>
  <div class="price-box"></div>
  <div class="price standard">
    <div class="art" role="img" aria-label="Illustration of a person with a coin"></div>
    <h3>$160 PER PERSON</h3>
    <p>+ $50 for additional persons<br>in same booking</p>
  </div>
  <div class="price early">
    <div class="art" role="img" aria-label="Illustration of an early bird with a coin"></div>
    <h3>$130 EARLYBIRD PRICE</h3>
    <p>FOR PAYMENTS BEFORE<br>15 FEB</p>
  </div>
  <div class="deadline">REGISTRATIONS CLOSE 22ND MARCH 2023</div>

  <p class="more center">For more information and to register please visit our website:<br><a href="#">https://quietvoicesclinic.com.au/webinar-school-treatment/</a></p>

  <div class="rule" style="top:2582px"></div>
  <h3 class="alt-title center">Can't make this date or time for the live webinar?</h3>
  <p class="alt-body">We got you covered! You can alternatively purchase the webinar in a USB package here or 4-week online access here.&nbsp; Please email or call 02 5550 1234 to order. NB. Participants who attend the live webinar will not have access to a recording.</p>
  <div class="rule" style="top:2783px"></div>

  <div class="series">
    <p>The Quiet Voices Clinic run a webinar series each year for parents, teachers, school support teams, and health professionals.</p>
    <p>All webinars are available in three formats: 1) A live webinar, 2) a USB package, 3) an online recording.&nbsp; For the full range of webinars, <a href="#">see here:</a></p>
  </div>

  <footer class="footer">
    <p style="top:43px">Copyright © | 2022 | Quiet Voices Clinic | All rights reserved.</p>
    <p style="top:79px">Our contact details are:</p>
    <p style="top:102px"><a href="#">workshops@quietvoicesclinic.com.au</a></p>
    <p style="top:139px"><a href="#">www.quietvoicesclinic.com.au</a></p>
    <p style="top:161px">12/88 Harbour Rd Northgate NSW 2999</p>
    <p style="top:182px">Phone: 02 5550 1234</p>
    <p class="unsub" style="top:231px"><a href="#">Unsubscribe here</a></p>
  </footer>

  <p class="follow center">Follow along with us</p>
  <div class="social" aria-label="Social links"><span></span><span></span><span></span></div>
</main>
</body>
</html>
```